Makeup Artist Requires Business Card design

Hi

I am looking for a business card design to market my makeup artist business. I operate under my own name Mara Veldt and I would like to keep the design of the card very simplistic and chic - something that keeps both my name and profession (makeup artist) the focus of the card. I would like it to be a style that is eyecatching to the reader (i am open to anything unusual) but upmarket.

Target Market(s)

women, magazine/beauty/fashion editors, photographers.

Industry/Entity Type

Business

Requirements
Must have
• Must contain:

Phone number: 0418 372 915
Website: www.maraveldt.com.au
email: contact@maraveldt.com.au

(although you don't need to have prefaced these with the words phone number, website etc :))
Should not have
• I am not looking for anything overly colorful - my preference is to keep the card dark if possible.

```html
<!DOCTYPE html>
<html lang="en">
<head>
<meta charset="utf-8">
<title>Mara Veldt – Make-Up Artist Business Card</title>
<link rel="stylesheet" href="https://fonts.googleapis.com/css2?family=Great+Vibes&family=Advent+Pro:wght@400;500&display=swap">
<style>
  :root {
    --page-bg: #2e2424;
    --card-bg: #4a4a4a;
    --name-ink: #1c1c1c;
    --role-ink: #3b3b3b;
    --contact-ink: #ececec;
  }
  * { margin: 0; padding: 0; box-sizing: border-box; }
  html, body {
    width: 1200px;
    height: 900px;
    overflow: hidden;
    background: var(--page-bg);
  }
  .canvas {
    position: relative;
    width: 1200px;
    height: 900px;
  }
  .business-card {
    position: absolute;
    left: 170px;
    top: 167px;
    width: 900px;
    height: 581px;
    background: var(--card-bg);
    border-radius: 5px;
  }
  .card-name {
    position: absolute;
    left: 0;
    right: 0;
    top: 150px;
    text-align: center;
    font-family: "Great Vibes", cursive;
    font-weight: 400;
    font-size: 150px;
    line-height: 1;
    color: var(--name-ink);
  }
  .card-role {
    position: absolute;
    left: 0;
    right: 0;
    top: 410px;
    text-align: center;
    font-family: "Advent Pro", sans-serif;
    font-weight: 500;
    font-size: 36px;
    letter-spacing: 3px;
    color: var(--role-ink);
  }
  .contact-row {
    position: absolute;
    left: 44px;
    right: 50px;
    top: 540px;
    display: flex;
    justify-content: space-between;
    align-items: center;
  }
  .contact-item {
    display: flex;
    align-items: center;
    gap: 12px;
    font-family: "Advent Pro", sans-serif;
    font-weight: 400;
    font-size: 19px;
    text-transform: uppercase;
    color: var(--contact-ink);
  }
  .contact-icon {
    width: 24px;
    height: 24px;
    fill: var(--contact-ink);
  }
</style>
</head>
<body>
<div class="canvas">
  <section class="business-card">
    <h1 class="card-name">Mara Veldt</h1>
    <p class="card-role">Make-Up Artist</p>
    <div class="contact-row">
      <div class="contact-item contact-phone">
        <svg class="contact-icon" viewBox="0 0 24 24" aria-hidden="true">
          <path d="M6.6 2c.6 0 1 .3 1.2.8l1.6 3.8c.2.5 0 1-.4 1.4L7.4 9.4c1 2.7 3.2 5.3 5.6 6.9l1.4-1.5c.4-.4.9-.5 1.4-.3l3.7 1.7c.5.2.8.7.7 1.3l-.4 2.8c-.1.6-.6 1-1.2 1C10 21.3 2.8 13.7 3 4.3c0-.6.4-1.1 1-1.2z"/>
        </svg>
        <span>0418 372 915</span>
      </div>
      <div class="contact-item contact-web">
        <svg class="contact-icon" viewBox="0 0 24 24" aria-hidden="true">
          <path d="M2 3h20v14H2zM4 5v10h16V5zM10 17h4l1 3h2v1.5H7V20h2z"/>
        </svg>
        <span>www.maraveldt.com.au</span>
      </div>
      <div class="contact-item contact-email">
        <svg class="contact-icon" viewBox="0 0 24 24" aria-hidden="true">
          <path d="M2 5h20v14H2zM4 7.2v9.6l4.8-4.8zM19.9 7H4.1L12 13.2zM20 7.2 15.2 12l4.8 4.8zM9.9 13 4.2 17h15.6l-5.7-4-2.1 1.6z"/>
        </svg>
        <span>contact@maraveldt.com.au</span>
      </div>
    </div>
  </section>
</div>
</body>
</html>
```